Marisol Specialty Coffee needs a Packaging design

We need packaging design for coffee that suits our brand identity, that is the best quality in Mexico.
We only sell mexican coffee with Q scores above 80
We are evaluating 3 types of packaging: Bag, Box and Cillinder can
The specific package format will be decided based on the designs that we get.
Updates

Target Market(s)

Coffee experts and enthusiast.
People that relate the Coffee consumption and experience with wine tasting and Bon Vivant way

Requirements
Should not have
• Photos any mexican cliché

```html
<!DOCTYPE html>
<html lang="en">
<head>
<meta charset="utf-8">
<title>Marisol Specialty Coffee – Label</title>
<link rel="stylesheet" href="https://fonts.googleapis.com/css2?family=Open+Sans:wght@300;400&display=swap">
<style>
  :root {
    --backdrop: #f4f1ec;
    --coffee-brown: #4e3426;
    --swirl-mid: #7a5c4a;
    --label-cream: #f3f1ec;
    --ink-brown: #3f2a1f;
  }
  html, body {
    margin: 0;
    padding: 0;
    width: 1200px;
    height: 1000px;
    overflow: hidden;
    background: var(--backdrop);
  }
  .canvas {
    position: relative;
    width: 1200px;
    height: 1000px;
  }
  .label {
    position: absolute;
    left: 420px;
    top: 40px;
    width: 360px;
    height: 920px;
    background: var(--coffee-brown);
    box-sizing: border-box;
  }
  .swirl-band {
    position: absolute;
    left: 0;
    top: 0;
    width: 360px;
    height: 290px;
    background: radial-gradient(circle at 35% 40%, var(--swirl-mid) 0%, var(--coffee-brown) 70%);
  }
  .brand-panel {
    position: absolute;
    left: 9px;
    top: 290px;
    width: 342px;
    height: 621px;
    background: var(--label-cream);
  }
  .brand-name {
    position: absolute;
    left: 60px;
    top: 60px;
    height: 500px;
    writing-mode: vertical-rl;
    transform: rotate(180deg);
    font-family: "Open Sans", sans-serif;
    font-weight: 400;
    font-size: 120px;
    line-height: 1;
    color: var(--ink-brown);
    text-align: center;
    letter-spacing: 2px;
  }
  .descriptor {
    position: absolute;
    left: 232px;
    top: 60px;
    height: 500px;
    writing-mode: vertical-rl;
    transform: rotate(180deg);
    display: flex;
    align-items: center;
    justify-content: center;
    gap: 14px;
    font-family: "Open Sans", sans-serif;
    font-weight: 400;
    font-size: 22px;
    letter-spacing: 3px;
    color: var(--ink-brown);
  }
  .descriptor-rule {
    display: block;
    width: 1px;
    height: 40px;
    background: var(--ink-brown);
  }
</style>
</head>
<body>
<main class="canvas">
  <section class="label">
    <div class="swirl-band" role="img" aria-label="Decorative cream swirl pattern on coffee brown"></div>
    <div class="brand-panel">
      <div class="brand-name">Marisol</div>
      <div class="descriptor">
        <span class="descriptor-rule"></span>
        <span>SPECIALTY COFFEE</span>
        <span class="descriptor-rule"></span>
      </div>
    </div>
  </section>
</main>
</body>
</html>
```